Bakery Business Cards

We are in need of business cards for our bakery business--something non-generic that reflects our business and will stand out. We are a wholesale bakery that primarily services in-store bakeries, casinos, schools, distributors, and fund-raising companies. The family business was founded in 1960. (www.marlowsovenworks.com)

```html
<!DOCTYPE html>
<html lang="en">
<head>
<meta charset="utf-8">
<title>Marlow's Ovenworks – Business Cards</title>
<link href="https://fonts.googleapis.com/css2?family=Montserrat+Alternates:wght@400;600&display=swap" rel="stylesheet">
<style>
  :root {
    --bg: #e0e0e0;
    --brand-blue: #2446a6;
    --brand-blue-deep: #1e3c92;
    --white: #ffffff;
    --wood-light: #e3cba4;
    --wood: #d4b183;
    --cream: #ece6dc;
    --veil: rgba(255, 255, 255, 0.62);
  }
  * { margin: 0; padding: 0; box-sizing: border-box; }
  html, body {
    width: 1200px; height: 800px; overflow: hidden;
    background: var(--bg);
    font-family: "Montserrat Alternates", "Trebuchet MS", sans-serif;
  }
  .canvas {
    position: relative; width: 1200px; height: 800px;
    display: flex; align-items: center; justify-content: center; gap: 40px;
  }
  .card {
    position: relative; width: 530px; height: 303px;
    border-radius: 32px; overflow: hidden;
  }
  /* Front */
  .card-front__photo {
    position: absolute; inset: 0;
    background: linear-gradient(125deg, var(--cream) 0%, var(--wood-light) 45%, var(--wood) 100%);
  }
  .card-front__veil {
    position: absolute; left: 90px; top: 70px; width: 350px; height: 165px;
    border-radius: 60px; background: var(--veil);
  }
  .card-front__brand {
    position: absolute; left: 90px; top: 70px; width: 350px; height: 165px;
    display: flex; flex-direction: column; align-items: center; justify-content: center;
    color: var(--brand-blue);
  }
  .brand-name {
    font-weight: 600; font-size: 34px; line-height: 1.1; text-align: center;
  }
  .brand-since {
    margin-top: 8px; font-weight: 600; font-size: 14px; letter-spacing: 0.12em;
    text-transform: uppercase;
  }
  /* Back */
  .card-back { background: var(--brand-blue); color: var(--white); }
  .card-back__pattern {
    position: absolute; inset: 0;
    background: linear-gradient(160deg, var(--brand-blue), var(--brand-blue-deep));
  }
  .card-back__brand {
    position: absolute; left: 34px; top: 0; bottom: 0; width: 210px;
    display: flex; flex-direction: column; justify-content: center; align-items: center;
  }
  .card-back__brand .brand-name { font-size: 28px; }
  .card-back__brand .brand-since { font-size: 12px; }
  .contact {
    position: absolute; left: 262px; top: 62px; width: 250px;
    font-style: normal; font-size: 13px; line-height: 1.4; font-weight: 400;
  }
  .contact__phone { font-size: 18px; font-weight: 600; letter-spacing: 0.04em; }
  .contact__block { margin-top: 12px; }
</style>
</head>
<body>
<main class="canvas">
  <section class="card card-front">
    <div class="card-front__photo" role="img" aria-label="Overhead photo of slices of berry and peach pie on white plates on a wooden table"></div>
    <div class="card-front__veil"></div>
    <div class="card-front__brand">
      <p class="brand-name">Marlow's<br>Ovenworks</p>
      <p class="brand-since">Since 1960</p>
    </div>
  </section>

  <section class="card card-back">
    <div class="card-back__pattern" role="img" aria-label="Faint outline pattern of baked goods on royal blue"></div>
    <div class="card-back__brand">
      <p class="brand-name">Marlow's<br>Ovenworks</p>
      <p class="brand-since">Since 1960</p>
    </div>
    <address class="contact">
      <p class="contact__phone">405.555.0182</p>
      <p>hello@marlowsovenworks.com</p>
      <p class="contact__block">1187 Juniper Ave<br>Oklahoma City, OK 73110</p>
      <p class="contact__block">Mailing address:<br>PO Box 62019<br>Yukon, OK 73099</p>
    </address>
  </section>
</main>
</body>
</html>
```